AMBER AND STONE WEB

We need a home design in wordpress, we have now a web but we would like to improve it. Our current web is www.amberandstonevillas.example Our business is holliday rental of villas in Ibiza. Our guest must know that we are a reliable company, professional and with experience and good reviews. We want them to click in our reservation engine: https://bookings.amberandstonevillas.example/en/ and make reservation in our website. We would also like to say that all the properties that we have are just us who commercialize so we have best price available. Many people are going to see our villas in staylister.example and look to our website to make a reservation with us so we need to show them that they are at the right place and click at our link to our reservation engine. What make us special is that we are a local company, we are from Ibiza, Our guests are always received in person by the Amber and Stone Villas team. You will enjoy extensive tourist information when you check in and during the entire stay. You will be attended by ChatLoop and calls, always happy to help so that you have a happy and fun stay! Our guest stay is better than in hotel as they have more spece, private swiming pool, private garden, barbeque ... To rent a villa is the best way to stay in Ibiza. We also have a promotional video: https://vidshare.example/Qm7tLp2Xz9A Let our philosophy be shown, we think that coming on holiday to Ibiza implies seeing the nature that we have in Ibiza, hence our name AMBER AND STONE, like the pins that almost touch the sea in Ibiza, or the posidonea meadows where the intense green of the seaweed and the blue of the sea. We are aware of the environment, and we love Ibiza. For us, the client who visits Ibiza, should rent a car, go around the island, eat in a restaurant one day in front of the sea, is a night of partying to the discs, go shopping, visit the ancient heritage of Umanity, make some aquatic sport, enjoy the pool, those are for us Ibiza.

Target Market(s)

Europe, people from Holand, UK, Germany, France, Spain ...

Industry/Entity Type

Tourism

Colors

Designer to choose colors to be used in the design.

Requirements
Must have
• Pictures of Ibiza.
Nice to have
• Our name Amber and Stone Villas is beacuse in Ibiza there is forest that almost touch the watter of the Mediterranean sea, so you can see green of the forest and blue of the sea and the sky. And also beacause under the watter of the sea there is a plant called Posidonia that is also green please see the picture of posidonia.

```html
<!DOCTYPE html>
<html lang="en">
<head>
<meta charset="utf-8">
<title>Amber and Stone Villas Ibiza</title>
<link href="https://fonts.googleapis.com/css2?family=Open+Sans:ital,wght@0,400;0,600;0,700;0,800;1,400&display=swap" rel="stylesheet">
<style>
:root{
  --green:#6f9a2a;
  --green-dark:#4f7a1c;
  --green-light:#8cb83a;
  --green-text:#8bbd2c;
  --ink:#2a2a2a;
  --body:#555;
  --white:#fff;
  --sea:#1a6fc0;
  --night:#151a1c;
  --star:#f29a1e;
}
*{margin:0;padding:0;box-sizing:border-box}
html,body{width:1200px;height:3318px;overflow:hidden;background:var(--white)}
body{font-family:"Open Sans",Arial,sans-serif;color:var(--body);position:relative}
.abs{position:absolute}
.btn{position:absolute;display:flex;align-items:center;justify-content:center;background:linear-gradient(#7ea52f,#557f1e);color:var(--white);font-weight:700;font-size:15px;letter-spacing:.5px;border-radius:2px;text-transform:uppercase}

/* hero */
.hero{left:0;top:0;width:1200px;height:680px;background:linear-gradient(180deg,#1a2d7a 0%,#2a5fb6 22%,#1f7fc8 45%,#2ea8d8 62%,#3b7a3a 80%,#5a7a34 100%)}
.hero-wave{left:0;top:600px;width:1200px;height:90px}
.brand{left:75px;top:62px;display:flex;align-items:center;gap:10px;color:var(--white);font-weight:600;font-size:22px;letter-spacing:.5px}
.brand-dot{width:26px;height:26px;border-radius:50%;background:var(--green-light)}
.nav{left:610px;top:56px;display:flex;gap:40px;font-size:13px;font-weight:700;color:var(--white);letter-spacing:.4px}
.nav .active{color:var(--green-light)}
.nav-book{left:1036px;top:46px;width:91px;height:38px;font-size:13px}
.hero-title{left:0;top:290px;width:1200px;text-align:center;color:var(--white);font-weight:800;font-size:58px;line-height:56px;letter-spacing:1px;text-shadow:0 2px 6px rgba(0,0,0,.35)}
.hero-arrow{top:329px;width:40px;height:40px;border:2px solid var(--white);border-radius:50%}
.hero-arrow svg{width:36px;height:36px}

/* booking */
.booking{left:75px;top:608px;width:1050px;height:186px;background:#f6f6f6;border:5px solid var(--green)}
.booking h2{position:absolute;left:0;top:40px;width:100%;text-align:center;font-size:24px;font-weight:600;color:var(--ink);letter-spacing:1px}
.field{position:absolute;top:94px;height:49px;background:var(--white);border:1px solid #cfcfcf;font-size:12px;font-weight:600;color:#333;display:flex;align-items:center;justify-content:space-between;padding:0 12px}
.field svg{width:12px;height:12px}
.book-now{left:866px;top:94px;width:153px;height:49px;font-size:16px}

/* intro */
.intro-title{left:0;top:847px;width:1200px;text-align:center;font-size:25px;font-weight:700;color:var(--ink);letter-spacing:.5px}
.intro-text{left:100px;top:907px;width:1000px;text-align:center;font-size:15.5px;line-height:27px}
.intro-btn{left:524px;top:1017px;width:152px;height:45px}

/* experiences */
.exp-bg{left:0;top:1120px;width:1200px;height:530px}
.exp{position:absolute;width:260px;text-align:center;color:var(--white);font-weight:700;font-size:15.5px;line-height:22px}
.exp .ring{width:94px;height:94px;border:3px solid var(--white);border-radius:50%;margin:0 auto 14px;display:flex;align-items:center;justify-content:center}
.exp svg{width:44px;height:44px}

/* video */
.video-title{left:0;top:1690px;width:1200px;text-align:center;font-size:25px;font-weight:700;color:var(--ink);letter-spacing:.5px}
.video{left:216px;top:1752px;width:769px;height:326px;background:radial-gradient(ellipse at 52% 60%,#2d5f86 0%,#2a3a48 30%,#3b3a3b 60%,#2e2c2d 100%)}
.play{left:357px;top:135px;width:56px;height:56px}

/* reviews */
.rev-bg{left:0;top:2130px;width:1200px;height:460px}
.rev-title{left:0;top:2208px;width:1200px;text-align:center;color:var(--white);font-size:25px;font-weight:700;letter-spacing:.5px}
.avatar{left:556px;top:2270px;width:88px;height:88px;border-radius:50%;border:3px solid var(--white);background:#c9c2bb}
.quote{left:200px;top:2376px;width:800px;text-align:center;color:var(--white);font-style:italic;font-size:17px;line-height:28px}
.rev-name{left:0;top:2438px;width:1200px;text-align:center;color:var(--green-text);font-weight:700;font-size:15px}
.stars{left:556px;top:2475px;width:88px;height:18px}
.rev-arrow{top:2332px;width:30px;height:36px}

/* philosophy */
.philo-photo{left:75px;top:2649px;width:512px;height:309px;background:linear-gradient(135deg,#2f4a1f 0%,#5b7a3a 45%,#8a8d5a 75%,#c2a45d 100%)}
.philo-title{left:614px;top:2664px;font-size:25px;font-weight:700;color:var(--ink);letter-spacing:.5px}
.philo-text{left:614px;top:2714px;width:510px;font-size:15.5px;line-height:28.6px}
.philo-btn{left:614px;top:2888px;width:152px;height:45px}

/* footer */
.foot-bg{left:0;top:3020px;width:1200px;height:298px}
.foot-brand{left:75px;top:3128px;display:flex;align-items:center;gap:10px;color:var(--green-light);font-weight:600;font-size:21px}
.copy{left:75px;top:3184px;color:#ddd;font-size:14px;line-height:22px}
.social{left:75px;top:3244px;display:flex;gap:14px}
.social span{width:22px;height:22px;border-radius:3px;background:#b8b8b8}
.foot-col{top:3116px;color:var(--white)}
.foot-col h3{font-size:16px;font-weight:700;letter-spacing:.5px;margin-bottom:8px}
.foot-col li{list-style:none;font-size:14px;line-height:28.5px;color:#ddd}
.foot-col .green{color:var(--green-text);font-weight:700;font-size:13.5px}
.foot-col svg{width:12px;height:12px;vertical-align:-1px;margin-right:7px}
.news-input{left:885px;top:3155px;width:242px;height:37px;background:var(--white);font-size:12px;color:#555;padding:11px 12px}
.news-btn{left:1036px;top:3203px;width:91px;height:39px;font-size:13px}
</style>
</head>
<body>

<!-- hero -->
<div class="abs hero" role="img" aria-label="Photo of an Ibiza cove with turquoise sea, sailing boats and pine-covered cliffs"></div>
<svg class="abs hero-wave" viewBox="0 0 1200 90" preserveAspectRatio="none"><path d="M0 40 C300 20 700 95 1200 55 L1200 90 L0 90Z" fill="#fff"/></svg>
<div class="abs brand"><span class="brand-dot"></span>AMBER AND STONE</div>
<nav class="abs nav"><span class="active">HOME</span><span>EXPERIENCE</span><span>ABOUT US</span><span>CONTACT US</span></nav>
<div class="btn nav-book">BOOK</div>
<h1 class="abs hero-title">THE BEST WAY TO STAY<br>IN IBIZA!</h1>
<div class="abs hero-arrow" style="left:75px"><svg viewBox="0 0 36 36"><path d="M21 10 L13 18 L21 26" stroke="#fff" stroke-width="2" fill="none"/></svg></div>
<div class="abs hero-arrow" style="left:1085px"><svg viewBox="0 0 36 36"><path d="M15 10 L23 18 L15 26" stroke="#fff" stroke-width="2" fill="none"/></svg></div>

<!-- booking -->
<section class="abs booking">
  <h2>BOOKING</h2>
  <div class="field" style="left:26px;width:330px">Best Available Rates</div>
  <div class="field" style="left:367px;width:153px">Check In<svg viewBox="0 0 12 12"><rect x="1" y="2" width="10" height="9" fill="none" stroke="#333"/><path d="M1 5h10M4 1v2M8 1v2" stroke="#333"/></svg></div>
  <div class="field" style="left:530px;width:154px">Check Out<svg viewBox="0 0 12 12"><rect x="1" y="2" width="10" height="9" fill="none" stroke="#333"/><path d="M1 5h10M4 1v2M8 1v2" stroke="#333"/></svg></div>
  <div class="field" style="left:696px;width:154px">No of People<svg viewBox="0 0 12 12"><path d="M3 5l3-3 3 3zM3 7l3 3 3-3z" fill="#333"/></svg></div>
  <div class="btn book-now">BOOK NOW</div>
</section>

<!-- intro -->
<h2 class="abs intro-title">VILLAS AND THE COUNTRYSIDE THE BEST OPTION TO STAY IN IBIZA</h2>
<p class="abs intro-text">Amber and Stone Villas is a company specialized in offering its clients accommodation in Villas on the countryside of Ibiza. Our guests enjoy the rural Ibiza, tranquility, relax, private pool, close to dream beaches and coves, the best restaurants, an unforgettable holiday for family or friends.</p>
<div class="btn intro-btn">READ MORE</div>

<!-- experiences -->
<svg class="abs exp-bg" viewBox="0 0 1200 530" preserveAspectRatio="none" role="img" aria-label="Green-tinted photo of Ibiza pine forest above the sea">
  <defs><linearGradient id="gexp" x1="0" y1="0" x2="1" y2="1"><stop offset="0" stop-color="#4f8a35"/><stop offset=".5" stop-color="#6aa23c"/><stop offset="1" stop-color="#86b63a"/></linearGradient></defs>
  <path d="M0 10 C250 70 700 -10 1200 30 L1200 520 C900 440 400 560 0 495Z" fill="url(#gexp)"/>
</svg>
<div class="exp" style="left:66px;top:1226px"><div class="ring"><svg viewBox="0 0 44 44"><path d="M8 26 L12 16 H32 L36 26 V33 H8Z" fill="#fff"/><circle cx="14" cy="33" r="3.5" fill="#6aa23c"/><circle cx="30" cy="33" r="3.5" fill="#6aa23c"/><rect x="14" y="18" width="16" height="6" fill="#6aa23c"/></svg></div>Should Rent<br>a Car</div>
<div class="exp" style="left:336px;top:1226px"><div class="ring"><svg viewBox="0 0 44 44"><path d="M22 14 L22 34" stroke="#fff" stroke-width="3"/><path d="M22 14 C14 8 8 12 6 16 C12 12 18 13 22 14 C26 8 34 8 38 14 C32 12 26 13 22 14Z" fill="#fff"/><path d="M8 36 C16 30 28 30 36 36Z" fill="#fff"/></svg></div>Go Around The<br>Island</div>
<div class="exp" style="left:605px;top:1226px"><div class="ring"><svg viewBox="0 0 44 44"><rect x="8" y="20" width="28" height="3" fill="#fff"/><path d="M12 23v12M32 23v12" stroke="#fff" stroke-width="3"/><rect x="19" y="11" width="6" height="9" fill="#fff"/></svg></div>A Restaurant One Day In<br>Front Of The Sea</div>
<div class="exp" style="left:874px;top:1226px"><div class="ring"><svg viewBox="0 0 44 44"><path d="M18 10 V28 M18 10 L32 7 V25" stroke="#fff" stroke-width="3" fill="none"/><circle cx="15" cy="30" r="4" fill="#fff"/><circle cx="29" cy="27" r="4" fill="#fff"/></svg></div>Is A Night Of Partying<br>To The Discos</div>
<div class="exp" style="left:66px;top:1411px"><div class="ring"><svg viewBox="0 0 44 44"><path d="M6 10 H11 L15 28 H33 L36 15 H13" stroke="#fff" stroke-width="3" fill="none"/><circle cx="17" cy="33" r="3" fill="#fff"/><circle cx="31" cy="33" r="3" fill="#fff"/></svg></div>Go<br>Shopping</div>
<div class="exp" style="left:336px;top:1411px"><div class="ring"><svg viewBox="0 0 44 44"><path d="M10 26 C10 14 34 14 34 26Z" fill="#fff"/><rect x="22" y="8" width="2" height="8" fill="#fff"/><rect x="8" y="26" width="28" height="10" fill="#fff"/><rect x="13" y="29" width="4" height="5" fill="#6aa23c"/><rect x="20" y="29" width="4" height="5" fill="#6aa23c"/><rect x="27" y="29" width="4" height="5" fill="#6aa23c"/></svg></div>Visit The Ancient Heritage<br>Of Humanity</div>
<div class="exp" style="left:605px;top:1411px"><div class="ring"><svg viewBox="0 0 44 44"><path d="M8 28 H36 L32 33 H12Z" fill="#fff"/><path d="M14 28 L22 18 H30 L28 28" fill="#fff"/><path d="M6 37 C12 34 16 40 22 37 C28 34 32 40 38 37" stroke="#fff" stroke-width="2.5" fill="none"/></svg></div>Make Some Aquatic<br>Sport</div>
<div class="exp" style="left:874px;top:1411px"><div class="ring"><svg viewBox="0 0 44 44"><path d="M16 30 V10 C16 6 21 6 21 10 M28 30 V10 C28 6 33 6 33 10" stroke="#fff" stroke-width="3" fill="none"/><path d="M16 16 H28 M16 23 H28" stroke="#fff" stroke-width="2.5"/><path d="M6 34 C12 30 16 38 22 34 C28 30 32 38 38 34" stroke="#fff" stroke-width="3" fill="none"/></svg></div>Enjoy The<br>Pool</div>

<!-- video -->
<h2 class="abs video-title">PROMO VIDEO</h2>
<div class="abs video" role="img" aria-label="Promotional video still, close-up in deep blue tones">
  <svg class="abs play" viewBox="0 0 56 56"><circle cx="28" cy="28" r="27" fill="#ddd"/><path d="M22 16 L40 28 L22 40Z" fill="#333"/></svg>
</div>

<!-- reviews -->
<svg class="abs rev-bg" viewBox="0 0 1200 460" preserveAspectRatio="none" role="img" aria-label="Darkened photo of an Ibiza harbour with moored boats">
  <defs><linearGradient id="grev" x1="0" y1="0" x2="0" y2="1"><stop offset="0" stop-color="#3c4848"/><stop offset=".5" stop-color="#2e4658"/><stop offset="1" stop-color="#243340"/></linearGradient></defs>
  <path d="M0 15 C250 60 650 -10 1200 40 L1200 420 C800 400 450 470 0 420Z" fill="url(#grev)"/>
</svg>
<h2 class="abs rev-title">CUSTOMER REVIEWS</h2>
<div class="abs avatar" role="img" aria-label="Guest portrait"></div>
<p class="abs quote">“ Vestibulum ante ipsum primis in faucibus<br>orci luctus et ultrices posuere cubilia egestas risus in magna varius..”</p>
<div class="abs rev-name">-Name Heading</div>
<svg class="abs stars" viewBox="0 0 88 18"><g fill="#f29a1e"><path id="st" d="M9 1l2.2 5.3 5.6.4-4.3 3.7 1.4 5.5L9 13l-4.9 2.9 1.4-5.5L1.2 6.7l5.6-.4Z"/><use href="#st" x="17.5"/><use href="#st" x="35"/><use href="#st" x="52.5"/><use href="#st" x="70"/></g></svg>
<svg class="abs rev-arrow" style="left:131px" viewBox="0 0 30 36"><path d="M20 6 L10 18 L20 30" stroke="#ddd" stroke-width="4" fill="none"/></svg>
<svg class="abs rev-arrow" style="left:1041px" viewBox="0 0 30 36"><path d="M10 6 L20 18 L10 30" stroke="#ddd" stroke-width="4" fill="none"/></svg>

<!-- philosophy -->
<div class="abs philo-photo" role="img" aria-label="Photo of the owner seated by a villa pool among cypress trees"></div>
<h2 class="abs philo-title">PHILOSOPHY</h2>
<p class="abs philo-text">Curabitur quis elit et ligula pharetra blandit sed quis duip hasellus luctus magna vitae hendrerit commodo. Vestibulum rhoncus nunc in ipsum molestie, id euismod mauris placerat. Suspendisse ac turpis in mauris tempor sodales. Nunc vehicula sapien eget ipsum congue, sit amet varius eros condimentum.</p>
<div class="btn philo-btn">READ MORE</div>

<!-- footer -->
<svg class="abs foot-bg" viewBox="0 0 1200 298" preserveAspectRatio="none"><path d="M0 50 C300 15 700 0 1200 20 L1200 298 L0 298Z" fill="#161b1c"/></svg>
<div class="abs foot-brand"><span class="brand-dot"></span>AMBER AND STONE</div>
<p class="abs copy">Copyright ©2019 Company Name<br>All Right Reserved</p>
<div class="abs social"><span></span><span></span><span></span><span></span><span></span></div>
<div class="abs foot-col" style="left:368px"><h3>SITE MAP</h3><ul><li>Home</li><li>Experience</li><li>All Properties</li><li>About Us</li><li>Contact Us</li></ul></div>
<div class="abs foot-col" style="left:614px"><h3>CONTACT INFO</h3><ul>
  <li class="green">AMBER AND STONE VILLAS IBIZA</li>
  <li style="line-height:22px;padding-top:4px">4120 Olive Grove Lane<br>Sant Josep, 07830</li>
  <li><svg viewBox="0 0 12 12"><rect x="0" y="0" width="12" height="12" rx="2" fill="#ddd"/><path d="M3 3 L5 3 L5.5 5 L4.5 6 C5 7 6 8 7 8.5 L8 7.5 L9.5 8 V9.5 C6 9.5 3 6.5 3 3Z" fill="#161b1c"/></svg>1-800-555-0142</li>
  <li><svg viewBox="0 0 12 12"><rect x="0" y="2" width="12" height="8" fill="#ddd"/><path d="M0 2 L6 7 L12 2" stroke="#161b1c" fill="none"/></svg>info@amberandstone.example</li>
</ul></div>
<div class="abs foot-col" style="left:886px"><h3>NEWSLETTER SIGN UP</h3></div>
<div class="abs news-input">Enter Email Address</div>
<div class="btn news-btn">SIGN UP</div>

</body>
</html>
```